Atelier Marrow Architecture business card

We need to update our business card. We do high end custom residential, hospitality, and wellness architecture. We focus on creating unique spaces and design around the five senses, believing that architecture's true impact is not on our surroundings, but within us. We would like to see designs are instill a sense of calm awe. They should be crisp, fresh, clean, authentic, & contemporary without being sterile, overworked, or harsh. White space is important. Alternative materials are an option if natural. We have created our own logo and would like designs to incorporate it. However, we are willing to see alternatives if the logo becomes a stumbling block and you have an alternate you suggest. Card must have the following information:
Atelier Marrow Architecture, Inc.
728 Holloway Ct. NE Atlanta, GA 30318
Marcus T. Whitcombe, AIA, NCARB, LEED AP BD+C
ateliermarrow.example

Target Market(s)

Higher net worth individuals with an appreciation for design, nature, sustainability,

Industry/Entity Type

Architect

Contact Information for Business Card

See above. The title of Owner or Architect is helpful but not necessary. Minimalism should trump additional information.

Font styles to use
Serif
Sans Serif

Requirements
Must have
• It should look professional. It must use logo
Should not have
• caligraphy, animals, anything that is cute,

```html
<!DOCTYPE html>
<html lang="en">
<head>
<meta charset="utf-8">
<title>Atelier Marrow Architecture — Business Card</title>
<link rel="stylesheet" href="https://fonts.googleapis.com/css2?family=Roboto:wght@300;400;500&display=swap">
<style>
  :root {
    --bg: #ecebe7;
    --paper: #ffffff;
    --paper-shade: #f1f1f1;
    --green: #1a9a55;
    --green-deep: #0e7d40;
    --green-light: #1fbf73;
    --ink-grey: #6b6b6b;
    --rule: #3f8f4f;
    --on-green: #f2fff7;
  }
  * { box-sizing: border-box; margin: 0; padding: 0; }
  html, body { width: 1200px; height: 1023px; overflow: hidden; }
  body {
    background: var(--bg);
    font-family: "Roboto", Arial, sans-serif;
    position: relative;
  }
  .card {
    position: absolute;
    left: 280px;
    width: 640px;
    height: 366px;
    border-radius: 14px;
    overflow: hidden;
    box-shadow: 0 6px 18px rgba(0,0,0,0.18);
  }
  /* Front */
  .card--front {
    top: 90px;
    background: linear-gradient(180deg, var(--paper-shade) 0%, var(--paper) 35%, var(--paper) 100%);
  }
  .front__brand {
    position: absolute;
    left: 44px;
    top: 128px;
    display: flex;
    align-items: center;
    gap: 10px;
  }
  .brand-dot {
    width: 12px; height: 12px;
    border-radius: 50%;
    background: var(--green);
    flex: none;
  }
  .brand-name {
    font-weight: 400;
    font-size: 16px;
    color: var(--green);
  }
  .front__person {
    position: absolute;
    right: 36px;
    top: 48px;
    width: 290px;
    text-align: right;
    border-bottom: 1px solid var(--rule);
    padding-bottom: 4px;
  }
  .person-name {
    font-weight: 500;
    font-size: 25px;
    color: var(--green);
  }
  .person-credentials {
    font-weight: 400;
    font-size: 12px;
    color: var(--ink-grey);
    letter-spacing: 0.03em;
    margin-top: 2px;
  }
  .front__contact {
    position: absolute;
    left: 44px;
    bottom: 66px;
    width: 260px;
    border-top: 1px solid var(--rule);
    padding-top: 8px;
    font-size: 12.5px;
    color: var(--ink-grey);
    line-height: 1.45;
  }
  .contact-line { display: flex; align-items: center; gap: 7px; }
  .contact-line svg { width: 12px; height: 12px; flex: none; }
  .contact-gap { margin-top: 6px; }
  .front__band {
    position: absolute;
    left: 0; right: 0; bottom: 0;
    height: 44px;
    background: var(--green);
    display: flex;
    align-items: center;
    justify-content: flex-end;
    padding-right: 36px;
  }
  .band-url {
    color: var(--on-green);
    font-size: 14px;
    letter-spacing: 0.06em;
  }
  /* Back */
  .card--back {
    top: 540px;
    background: radial-gradient(ellipse at 55% 45%, var(--green-light) 0%, var(--green) 50%, var(--green-deep) 100%);
    display: flex;
    align-items: center;
    justify-content: center;
  }
  .back__brand {
    display: flex;
    align-items: center;
    gap: 12px;
  }
  .back__dot {
    width: 14px; height: 14px;
    border-radius: 50%;
    background: var(--on-green);
    flex: none;
  }
  .back__name {
    font-weight: 300;
    font-size: 26px;
    color: var(--on-green);
  }
</style>
</head>
<body>
  <section class="card card--front" aria-label="Business card front">
    <div class="front__brand">
      <span class="brand-dot"></span>
      <span class="brand-name">Atelier Marrow Architecture</span>
    </div>

    <div class="front__person">
      <p class="person-name">Marcus T. Whitcombe</p>
      <p class="person-credentials">AIA, NCARB, LEED AP BD+C</p>
    </div>

    <div class="front__contact">
      <p>728 Holloway Ct. NE</p>
      <p>Atlanta, GA 30318</p>
      <p class="contact-line contact-gap">
        <svg viewBox="0 0 12 12" aria-hidden="true"><circle cx="6" cy="6" r="5.3" fill="none" stroke="#1a9a55" stroke-width="1"/><path d="M4 3.3l1 1.2-.6.8c.4.8 1 1.4 1.8 1.8l.8-.6 1.2 1-.6 1c-2.2-.3-4-2.1-4.3-4.3z" fill="#1a9a55"/></svg>
        404 555 0178
      </p>
      <p class="contact-line">
        <svg viewBox="0 0 12 12" aria-hidden="true"><rect x="0.5" y="2" width="11" height="8" fill="#1a9a55"/><path d="M0.5 2l5.5 4.5L11.5 2" fill="none" stroke="#fff" stroke-width="1"/></svg>
        info@ateliermarrow.example
      </p>
    </div>

    <div class="front__band">
      <span class="band-url">www.ateliermarrow.example</span>
    </div>
  </section>

  <section class="card card--back" aria-label="Business card back">
    <div class="back__brand">
      <span class="back__dot"></span>
      <span class="back__name">Atelier Marrow Architecture</span>
    </div>
  </section>
</body>
</html>
```